4' x 8' Construction Project Sign, think of a very large business card

We need project signs for our construction sites, the sign will be mounted along the road so cars driving by can quickly read. the sign should be able to be read as cars drive by doing highway speed.

Think like your making a large business card

I would like to include "NOW HIRING" Superintendents, Project Managers, Pipe Foremen, Pipe Layers, and Equipment Operators

Description of services we provide should include

Civil Construction Services
Land Clearing
Excavation
Underground Utilities
Environmental Maintenance

The 2 objectives is to market to future clients and to recruit new employees

The sign will be mounted on posts at the entrance of our construction projects
Updates

Low design quality

Target Market(s)

Construction and land developers

Industry/Entity Type

Construction Company

Other font styles liked:
• Hypatia Sans Pro lite

Colors

Designer to choose colors to be used in the design.

Requirements
Must have
• Clean and easy to read
• Civil Construction Services
• Land Clearing
• Excavation
• Underground Utilities
• Road Construction

```html
<!DOCTYPE html>
<html lang="en">
<head>
<meta charset="utf-8">
<title>Harlow Brothers Civil Construction – Project Sign</title>
<link rel="stylesheet" href="https://fonts.googleapis.com/css2?family=Jost:wght@300;400;500&family=Roboto:wght@700&family=Roboto+Condensed:ital,wght@1,700&display=swap">
<style>
  :root {
    --brand-blue: #26427f;
    --mist-grey: #e4e4e4;
    --sign-white: #ffffff;
    --hiring-yellow: #f6e500;
    --ink: #222222;
  }
  * { margin: 0; padding: 0; box-sizing: border-box; }
  html, body { width: 1200px; height: 2397px; overflow: hidden; background: var(--sign-white); }
  .sign { position: relative; width: 1200px; height: 2397px; overflow: hidden; font-family: "Jost", sans-serif; }
  .sign__backdrop { position: absolute; inset: 0; }
  .header {
    position: absolute; left: 0; top: 0; width: 1200px; height: 321px;
    background: var(--brand-blue); border-radius: 0 0 52px 52px;
    color: var(--sign-white); text-align: center;
  }
  .header__name { position: absolute; top: 42px; width: 100%; font-weight: 500; font-size: 104px; line-height: 1; letter-spacing: 1px; }
  .header__trade { position: absolute; top: 178px; width: 100%; font-weight: 400; font-size: 66px; line-height: 1; letter-spacing: 15px; padding-left: 15px; }
  .services { position: absolute; left: 64px; top: 392px; list-style: none; color: var(--brand-blue); font-weight: 400; font-size: 64px; line-height: 116px; letter-spacing: -0.5px; }
  .wordmark {
    position: absolute; left: 0; top: 1200px; width: 100%;
    display: flex; justify-content: center; align-items: center; gap: 22px;
    color: var(--brand-blue); font-weight: 500; font-size: 58px; line-height: 1; letter-spacing: 2px;
  }
  .wordmark__square { width: 44px; height: 44px; background: var(--brand-blue); }
  .hiring { position: absolute; top: 1588px; width: 100%; text-align: center; font-family: "Roboto", sans-serif; font-weight: 700; font-size: 168px; line-height: 1; letter-spacing: 10px; color: var(--hiring-yellow); }
  .roles { position: absolute; top: 1778px; left: 96px; width: 1050px; list-style: none; display: grid; grid-template-columns: 621px 1fr; row-gap: 44px; font-family: "Roboto Condensed", sans-serif; font-style: italic; font-weight: 700; font-size: 55px; line-height: 72px; color: var(--sign-white); }
  .roles li::before { content: "•"; margin-right: 6px; }
  .contact {
    position: absolute; left: 52px; top: 2157px; width: 1098px; height: 191px;
    background: var(--sign-white); border-radius: 44px;
    display: flex; align-items: center; justify-content: center;
    font-weight: 300; font-size: 86px; color: var(--ink); letter-spacing: 1px;
  }
</style>
</head>
<body>
<main class="sign">
  <svg class="sign__backdrop" width="1200" height="2397" viewBox="0 0 1200 2397" aria-hidden="true">
    <polygon points="0,1051 600,1546 1200,1051 1200,1242 600,1546 0,1242" fill="var(--mist-grey)"/>
    <polygon points="0,1242 600,1546 1200,1242 1200,2397 0,2397" fill="var(--brand-blue)"/>
  </svg>

  <header class="header">
    <h1 class="header__name">HARLOW BROTHERS</h1>
    <p class="header__trade">CIVIL CONSTRUCTION</p>
  </header>

  <ul class="services">
    <li>CIVIL CONSTRUCTION SERVICES</li>
    <li>- LAND CLEARING</li>
    <li>- EXCAVATION</li>
    <li>- UNDERGROUND UTILITIES</li>
    <li>- ROAD CONSTRUCTION</li>
    <li>- ENVIRONMENTAL MAINTENANCE</li>
  </ul>

  <div class="wordmark"><span class="wordmark__square"></span><span>HARLOW BROTHERS</span></div>

  <h2 class="hiring">NOW HIRING</h2>

  <ul class="roles">
    <li>SUPERINTENDENTS</li>
    <li>PIPE FOREMEN</li>
    <li>PROJECT MANAGERS</li>
    <li>PIPE LAYERS</li>
    <li>EQUIPMENT OPERATORS</li>
  </ul>

  <div class="contact">PHONE NUMBER HERE</div>
</main>
</body>
</html>
```